Billboard design

Loom Bath Sage, needs a new design for 10' x 40' billboard. The design picked will also be used on a 2014 white Corvane Trellis Van.

Design needs to be clean and easy to read and include existing logo and phone number...256-555-0147. We specialize in washing rugs...not carpet cleaning, so don't submit designs of a carpet cleaning machine on rugs. Rugs are submerged in water in a pit, scrubbed, rinsed and extracted. Most rugs are dirty due to pet problems. This is our 25th year in business so that may also be included. Our customers are generally higher end income women over 30.

Simply put our logo as the largest print, with the phone number second largest. No other text is needed. Just layout and graphics. Ideally a rug with an animal on it, or a dirty rug with dog, dirty dog, dog scooting on rug, food spill, etc...

I also would be interested in seeing a billboard that looks like an oriental rug with the center faded out with our logo. Rug needs to look very high end. I don't want clip art or a cartoony look.

Keep in mind that this same look will be used on all company vans.
Updates

                                       Our logo should be the only text, besides the phone number.  I just need graphics and a nice clean layout, that is very easy to read from the road.  25 yrs can also be included.

Please make sure my logo is very large.  If you put in a photo of a rug, make sure it looks like a rug and not wall to wall carpet.                                   

Reason: On vacation till Tue. 18.

Reason: Not happy with designs so far. Lots of the designs sent look as though a child sent them. There are a couple that are good. In addition to the brief that I left earlier, I would like to see maybe a sketch of a mischievous dog on a simple sketched rug. Could possibly use this as a mascot. I am considering getting rid of the blue drop in the logo. VERY SIMPLE clean design with very few lines in the sketch.

Target Market(s)

Women over 30, higher income

Industry/Entity Type

Pet

Requirements
Nice to have
• Dog on oriental rug, scooting, or dirty, or funny face etc...
Should not have
• Cartoon

```html
<!DOCTYPE html>
<html lang="en">
<head>
<meta charset="utf-8">
<title>Loom Bath Sage – Billboard 40x10</title>
<link rel="stylesheet" href="https://fonts.googleapis.com/css2?family=Open+Sans:ital,wght@1,400&family=Cormorant+Garamond:wght@500;600&family=Montserrat:wght@700&display=swap">
<style>
  :root {
    --page-bg: #cfd2d4;
    --blue-light: #2590d0;
    --blue-mid: #157bbd;
    --blue-deep: #0b5f98;
    --blue-edge: #0a4f82;
    --white: #ffffff;
    --logo-ink: #1f2a33;
    --photo-light: #e9ebec;
    --photo-mid: #9a9ea3;
    --photo-dark: #4b4a52;
  }
  * { box-sizing: border-box; margin: 0; padding: 0; }
  html, body {
    width: 1200px;
    height: 1105px;
    overflow: hidden;
    background: var(--page-bg);
  }
  .billboard {
    position: absolute;
    left: 40px;
    top: 412px;
    width: 1120px;
    height: 280px;
    overflow: hidden;
    color: var(--white);
  }
  .billboard-art {
    position: absolute;
    inset: 0;
  }
  .logo {
    position: absolute;
    left: 22px;
    top: 13px;
    display: flex;
    align-items: center;
    gap: 12px;
    color: var(--logo-ink);
    font-family: "Montserrat", sans-serif;
    font-weight: 700;
  }
  .logo-dot {
    width: 36px;
    height: 36px;
    border-radius: 50%;
    background: var(--blue-mid);
    flex: none;
  }
  .logo-name {
    display: block;
    font-size: 30px;
    line-height: 1;
    letter-spacing: -0.4px;
    white-space: nowrap;
  }
  .logo-sub {
    display: block;
    font-size: 8px;
    letter-spacing: 1.6px;
    text-transform: uppercase;
    margin-top: 5px;
    text-align: right;
  }
  .anniversary {
    position: absolute;
    left: 70px;
    top: 78px;
    width: 200px;
    height: 200px;
    font-family: "Cormorant Garamond", serif;
  }
  .anniversary-number {
    position: absolute;
    left: 8px;
    top: 32px;
    font-size: 170px;
    font-weight: 500;
    line-height: 1;
    letter-spacing: -14px;
    font-variant-numeric: lining-nums;
    font-feature-settings: "lnum" 1;
  }
  .anniversary-caption {
    position: absolute;
    left: 92px;
    top: -2px;
    line-height: 0.95;
    font-weight: 600;
  }
  .anniversary-caption .big { display: block; font-size: 23px; }
  .anniversary-caption .small { display: block; font-size: 14px; }
  .anniversary-year {
    position: absolute;
    left: 4px;
    top: 171px;
    font-size: 21px;
    font-weight: 500;
    letter-spacing: 2px;
    line-height: 1;
  }
  .tagline {
    position: absolute;
    right: 500px;
    top: 62px;
    text-align: right;
    font-family: "Open Sans", sans-serif;
    font-style: italic;
    font-weight: 400;
    line-height: 1.1;
  }
  .tagline-line { display: block; white-space: nowrap; }
  .tagline .soft { font-size: 17px; }
  .tagline .strong { font-size: 26px; }
  .tagline .second { font-size: 24px; }
  .phone {
    position: absolute;
    left: 250px;
    top: 219px;
    display: flex;
    align-items: center;
    gap: 12px;
  }
  .phone-icon { width: 34px; height: 38px; }
  .phone-number {
    font-family: "Montserrat", sans-serif;
    font-weight: 700;
    font-size: 37px;
    letter-spacing: 1px;
    line-height: 1;
    white-space: nowrap;
  }
</style>
</head>
<body>
  <section class="billboard" aria-label="Loom Bath Sage billboard">
    <svg class="billboard-art" width="1120" height="280" viewBox="0 0 1120 280">
      <defs>
        <linearGradient id="panel-blue" x1="0" y1="0" x2="1" y2="0">
          <stop offset="0" stop-color="#2590d0"/>
          <stop offset="0.45" stop-color="#157bbd"/>
          <stop offset="1" stop-color="#0b5f98"/>
        </linearGradient>
        <linearGradient id="photo-tones" x1="0" y1="0" x2="0" y2="1">
          <stop offset="0" stop-color="#9a9ea3"/>
          <stop offset="0.35" stop-color="#4b4a52"/>
          <stop offset="0.6" stop-color="#e9ebec"/>
          <stop offset="1" stop-color="#9a9ea3"/>
        </linearGradient>
      </defs>
      <rect class="panel" width="1120" height="280" fill="url(#panel-blue)"/>
      <path class="logo-tab" d="M0 0 H352 L337 60 Q334 70 323 70 H0 Z" fill="var(--white)"/>
      <path class="photo-edge-outer" d="M672 0 C622 90 628 200 668 280 H1120 V0 Z" fill="var(--blue-edge)"/>
      <path class="photo-edge-light" d="M682 0 C634 90 640 200 680 280 H1120 V0 Z" fill="var(--white)" opacity="0.85"/>
      <path class="photo-edge-inner" d="M688 0 C642 90 648 200 688 280 H1120 V0 Z" fill="var(--blue-mid)"/>
      <path class="photo" role="img" aria-label="Photo: a woman, a baby and a white puppy sitting on a white sheepskin rug in a modern living room with a grey sofa and a white rocking chair" d="M698 0 C654 90 660 200 698 280 H1120 V0 Z" fill="url(#photo-tones)"/>
    </svg>

    <div class="logo">
      <span class="logo-dot" aria-hidden="true"></span>
      <span class="logo-text">
        <span class="logo-name">Loom Bath Sage</span>
        <span class="logo-sub">Harbor Rinse, LLC</span>
      </span>
    </div>

    <div class="anniversary">
      <span class="anniversary-caption">
        <span class="big">We</span>
        <span class="big">Are</span>
        <span class="small">Celebrating</span>
      </span>
      <span class="anniversary-number">25</span>
      <span class="anniversary-year">YEAR</span>
    </div>

    <p class="tagline">
      <span class="tagline-line"><span class="soft">Let them to be </span><span class="strong">there world</span></span>
      <span class="tagline-line second">We care your rugs</span>
    </p>

    <div class="phone">
      <svg class="phone-icon" viewBox="0 0 34 38" aria-hidden="true">
        <rect x="3" y="3" width="15" height="32" rx="2.5" fill="none" stroke="#ffffff" stroke-width="2.4"/>
        <rect x="6.5" y="7" width="8" height="8" fill="#ffffff"/>
        <g fill="#ffffff">
          <rect x="6.5" y="19" width="2.2" height="2.2"/><rect x="9.9" y="19" width="2.2" height="2.2"/><rect x="13.3" y="19" width="2.2" height="2.2"/>
          <rect x="6.5" y="23" width="2.2" height="2.2"/><rect x="9.9" y="23" width="2.2" height="2.2"/><rect x="13.3" y="23" width="2.2" height="2.2"/>
          <rect x="6.5" y="27" width="2.2" height="2.2"/><rect x="9.9" y="27" width="2.2" height="2.2"/><rect x="13.3" y="27" width="2.2" height="2.2"/>
        </g>
        <path d="M23 14 Q26 19 23 24" fill="none" stroke="#ffffff" stroke-width="2" stroke-linecap="round"/>
        <path d="M27 11 Q32 19 27 27" fill="none" stroke="#ffffff" stroke-width="2" stroke-linecap="round"/>
      </svg>
      <span class="phone-number">256-555-0147</span>
    </div>
  </section>
</body>
</html>
```